Vortelan d.o.o. needes a web site design

We are a company dealing with automatic doors, industrial doors, roller shutters, access control systems.
We would like to get a design which is clean and neat, and here are some sites which work with similar products. These designs are some we like, but of course, I am looking for a design which is unique. We usually use grey and red colours, which you can see on www.vortelan.ba .
The sites we like are:
http://www.plexawin.com/gb/
http://www.brunosteca.it/eng/
http://faswoodportamel.com/

You have to understand, that we have 4 different groups of products, which are main groups. I would like if those 4 groups somehow could be in different colours. (Maybe "zuvex" colours), in order to separate the groups in some way.

Attached you have web site structure.

If any questions, please contact me.
Edvin

Target Market(s)

Bosnian market. Aluminium and PVC doors and window market, Construction companies, Supermarkets-Retail, Gas stations, Banks, Food industry, Heavy industry.

Industry/Entity Type

It Company

Contact Information for Business Card

I have attached our current business card in PDF. I weould like english on one side, bosnian on other side.

Logo Text

Vortelan is the name of the company, our core business is automation!

Number of Pages Required

5+ page

Font styles to use
Sans Serif

Colors
ec1f27
0792cd
9bcb3c
ffc214
ffffff

```html
<!DOCTYPE html>
<html lang="en">
<head>
<meta charset="UTF-8">
<title>Vortelan d.o.o. – Business Card</title>
<link rel="stylesheet" href="https://fonts.googleapis.com/css2?family=Questrial&display=swap">
<style>
  :root {
    --brand-red: #ec1f27;
    --brand-red-deep: #d9101c;
    --brand-grey: #4a4a4a;
    --card-white: #ffffff;
    --stage: #1f2a33;
    --stage-light: #3a4650;
  }
  * { margin: 0; padding: 0; box-sizing: border-box; }
  html, body { width: 1200px; height: 800px; overflow: hidden; }
  body {
    background: radial-gradient(ellipse at 60% 55%, var(--stage-light), var(--stage) 75%);
    font-family: "Questrial", sans-serif;
    position: relative;
  }
  .card {
    position: absolute;
    top: 250px;
    width: 520px;
    height: 297px;
    overflow: hidden;
    box-shadow: 0 18px 40px rgba(0,0,0,.45);
  }

  /* Back side */
  .card--back {
    left: 50px;
    background: linear-gradient(135deg, var(--brand-red-deep), var(--brand-red) 60%, #f4303a);
    color: var(--card-white);
    display: flex;
    flex-direction: column;
    align-items: center;
    justify-content: center;
    gap: 18px;
  }
  .back-wordmark {
    display: flex;
    align-items: center;
    gap: 14px;
    font-size: 58px;
    letter-spacing: 2px;
    line-height: 1;
  }
  .back-wordmark .mark-square {
    width: 30px; height: 30px;
    background: var(--card-white);
  }
  .back-url { font-size: 19px; letter-spacing: 2px; }

  /* Front side */
  .card--front {
    left: 630px;
    background: var(--card-white);
    display: flex;
  }
  .front-main {
    flex: 0 0 62%;
    padding: 30px 28px;
    position: relative;
  }
  .front-logo {
    display: flex;
    align-items: center;
    gap: 8px;
    color: var(--brand-red);
    font-size: 22px;
    letter-spacing: 1px;
  }
  .front-logo .mark-circle {
    width: 14px; height: 14px;
    border-radius: 50%;
    background: var(--brand-red);
  }
  .front-person {
    position: absolute;
    left: 28px;
    bottom: 64px;
  }
  .person-name {
    color: var(--brand-red);
    font-size: 36px;
    letter-spacing: 2px;
    line-height: 1;
  }
  .person-title {
    color: var(--brand-grey);
    font-size: 15px;
    letter-spacing: 1px;
    margin-top: 4px;
  }
  .front-contact {
    flex: 1;
    background: var(--brand-red);
    color: var(--card-white);
    padding: 26px 18px;
    font-size: 13px;
    line-height: 1.45;
    display: flex;
    flex-direction: column;
  }
  .contact-heading { font-size: 17px; margin-bottom: 4px; }
  .contact-phones { margin-top: 22px; }
  .contact-email { margin-top: auto; }
</style>
</head>
<body>
  <section class="card card--back" aria-label="Business card back">
    <div class="back-wordmark"><span class="mark-square"></span><span>vortelan</span></div>
    <div class="back-url">http://www.vortelan.ba/</div>
  </section>

  <section class="card card--front" aria-label="Business card front">
    <div class="front-main">
      <div class="front-logo"><span class="mark-circle"></span><span>vortelan d.o.o.</span></div>
      <div class="front-person">
        <div class="person-name">EDVIN</div>
        <div class="person-title">DIRECTOR GENERAL</div>
      </div>
    </div>
    <div class="front-contact">
      <div class="contact-heading">ADRESA:</div>
      <div class="contact-address">Brezova Aleja BB,<br>71300 KORAVA</div>
      <div class="contact-phones">
        T: (051) 314-620<br>
        F: (051) 314-621<br>
        M: (065) 482-913
      </div>
      <div class="contact-email">E: info@vortelan.ba</div>
    </div>
  </section>
</body>
</html>
```